Business Broker Website

Hi.
I need a new design done for a business broker website. An example of the style of website I like is https://marlowpartners.example/
The menu needs to be :
* Home
* Businesses for Sale
* What we do
* Our people
* Industries
* Blog
* Confidentiality
* Contact
The home page needs to include a section saying 'businesses sold' with each having a photo, heading and short description. It also needs to have a place to show a video which I have attached so you can take a screenshot to put it on the page.
The content on the home page needs to be as follows:
Venture Transfer Partners are a boutique brokerage business, specializing in the sales and marketing of SME businesses throughout Queensland and, the Northern Territory
who we are
Welcome to Venture Transfer Partners. Our specialization is in the marketing and acquisition of closely held businesses throughout Queensland and the Northern Territory. We concentrate in SME businesses in the turnovers of approximately $1,000,000 to $10,000,000 +.
The combined business experience and industry knowledge of our principal is unparalleled and fully committed to a “customer first always” approach to doing business.
Our seller’s benefit from a multi-faceted strategic marketing plan, custom prepared for each seller, no two marketing campaigns are the same. This assures maximum exposure to well-qualified Buyers, while strictly maintaining confidentiality.
We have the comprehensive knowledge and resources to help our Buyers identify their perfect business acquisition– perhaps even if that business is not currently listed for sale!
"the whole secret of a successful life is to find out what is one's destiny to do, and then do it." walter pimm
Target Market(s)
people looking to buy or sell businesses
Number of Pages Required
1 page
Look and feel

```html
<!DOCTYPE html>
<html lang="en">
<head>
<meta charset="utf-8">
<title>Venture Transfer Partners</title>
<link href="https://fonts.googleapis.com/css2?family=Roboto:wght@400;500;700&display=swap" rel="stylesheet">
<style>
:root{
  --purple:#5b4589;
  --purple-dark:#4a3574;
  --ink:#333;
  --muted:#666;
  --field:#ededed;
  --light:#f4f4f7;
  --footer:#efeff1;
  --white:#fff;
}
*{box-sizing:border-box;margin:0;padding:0}
html,body{width:1200px;height:4283px;overflow:hidden;background:var(--white)}
body{font-family:"Roboto",Arial,sans-serif;color:var(--ink);position:relative}
.abs{position:absolute}
.brand{display:flex;align-items:center;gap:12px;color:var(--purple);font-weight:700;font-size:34px;letter-spacing:-.3px}
.brand .dot{width:44px;height:44px;border-radius:50%;background:var(--purple)}
.site-header{left:0;top:0;width:1200px;height:103px}
.site-header .brand{position:absolute;left:146px;top:28px}
.phone{left:598px;top:36px;font-size:27px;color:var(--purple);font-weight:500;display:flex;align-items:center;gap:8px}
.btn{display:flex;align-items:center;justify-content:center;font-weight:700;font-size:16px;text-transform:uppercase;text-decoration:none}
.btn-solid{background:var(--purple);color:var(--white);border-radius:3px}
.header-cta{left:861px;top:27px;width:203px;height:53px}
.main-nav{left:0;top:103px;width:1200px;height:60px;background:var(--purple);display:flex;justify-content:center;gap:41px;align-items:center}
.main-nav a{color:var(--white);text-decoration:none;font-size:16px}
.hero{left:0;top:163px;width:1200px;height:548px;background:linear-gradient(100deg,#2a1457 0%,#3a1f78 35%,#1c2456 60%,#2b1a60 100%)}
.hero-title{left:66px;top:232px;color:var(--white);font-size:46px;font-weight:700;line-height:55px}
.hero-sub{left:67px;top:357px;width:410px;color:var(--white);font-size:15px;line-height:20px}
.lead-form{left:726px;top:163px;width:333px;height:590px;background:var(--white);border:4px solid var(--purple);border-top:none}
.lead-form h3{position:absolute;left:0;top:38px;width:100%;text-align:center;color:var(--purple);font-size:20px;font-weight:500;line-height:26px}
.field{position:absolute;left:33px;width:259px;height:47px;background:var(--field);font-size:13px;color:#888;padding:14px 16px}
.lead-form .btn{position:absolute;left:33px;top:495px;width:259px;height:53px;font-size:18px}
.who-frame{left:95px;top:869px;width:412px;height:386px;background:var(--purple)}
.who-photo{left:118px;top:894px;width:412px;height:482px;background:linear-gradient(160deg,#e7ecef,#b9c3cb 55%,#8c98a3)}
.section-title{color:var(--purple);font-size:46px;font-weight:700}
.who-title{left:573px;top:884px}
.who-copy{left:577px;top:964px;width:505px;font-size:15px;line-height:20px;color:var(--ink)}
.who-copy p{margin-bottom:20px}
.sold-band{left:0;top:1509px;width:1200px;height:439px;background:var(--purple)}
.sold-light{left:0;top:1948px;width:1200px;height:342px;background:var(--light)}
.sold-title{left:0;top:1582px;width:1200px;text-align:center;color:var(--white)}
.sold-sub{left:0;top:1653px;width:1200px;text-align:center;color:var(--white);font-size:15.5px;line-height:20px}
.sold-card{top:1737px;width:284px;height:447px;background:var(--white);box-shadow:0 2px 8px rgba(0,0,0,.08);text-align:center}
.sold-card .photo{height:211px;background:linear-gradient(160deg,#cfe3f5,#3d78b0 60%,#123a66)}
.sold-card h4{margin:38px 20px 0;color:var(--purple);font-size:24px;font-weight:700;line-height:27px}
.sold-card p{margin:14px 36px 0;color:var(--muted);font-size:15px;line-height:20px}
.video-title{left:0;top:2342px;width:1200px;text-align:center}
.video-sub{left:0;top:2420px;width:1200px;text-align:center;font-size:15.5px;line-height:20px;color:var(--ink)}
.video{left:229px;top:2505px;width:742px;height:409px;background:linear-gradient(180deg,#f1f1f1,#dfe6ec);overflow:hidden}
.video-bar{position:absolute;left:0;bottom:0;width:100%;height:60px;background:linear-gradient(0deg,rgba(0,0,0,.75),rgba(0,0,0,.3))}
.video-caption{position:absolute;left:130px;bottom:4px;width:480px;text-align:center;color:#ddd;font-size:19px;line-height:24px;background:rgba(0,0,0,.35)}
.time{position:absolute;bottom:42px;font-size:8px;color:#ddd}
.cta-band{left:0;top:2988px;width:1200px;height:303px;background:var(--purple)}
.cta-title{left:0;top:3050px;width:1200px;text-align:center;color:var(--white);font-size:42px;font-weight:500;line-height:52px}
.btn-outline{left:528px;top:3174px;width:143px;height:50px;border:1.5px solid var(--white);color:var(--white);border-radius:3px}
.overseas-title{left:151px;top:3415px}
.overseas-copy{left:151px;top:3487px;width:425px;font-size:15.5px;line-height:20px;color:var(--ink)}
.overseas-btn{left:151px;top:3711px;width:143px;height:50px}
.overseas-photo{left:630px;top:3384px;width:436px;height:436px;border-radius:50%;background:radial-gradient(circle at 40% 40%,#f2efe9,#c9c2b6 60%,#8a8277)}
.site-footer{left:0;top:3909px;width:1200px;height:374px;background:var(--footer)}
.foot-brand{left:151px;top:3990px}
.foot-about{left:151px;top:4088px;width:370px;font-size:15.5px;line-height:20px;color:var(--ink)}
.copyright{left:153px;top:4228px;font-size:14px;color:#888}
.foot-h{color:var(--purple);font-size:22px;font-weight:500}
.foot-links{left:592px;top:3988px}
.foot-links ul{list-style:none;margin-top:22px}
.foot-links li{font-size:13.5px;line-height:21px;color:var(--ink)}
.foot-contact{left:833px;top:3988px;width:280px}
.contact-row{display:flex;gap:12px;margin-top:22px;font-size:13.5px;line-height:20px;color:var(--ink)}
.contact-row svg{flex:none;margin-top:2px}
</style>
</head>
<body>

<header class="abs site-header">
  <div class="brand"><span class="dot"></span>Venture Transfer Partners</div>
  <div class="abs phone">
    <svg width="22" height="22" viewBox="0 0 24 24"><path fill="#5b4589" d="M6.6 10.8a15 15 0 0 0 6.6 6.6l2.2-2.2a1 1 0 0 1 1-.25 11.4 11.4 0 0 0 3.6.57 1 1 0 0 1 1 1V20a1 1 0 0 1-1 1A17 17 0 0 1 3 4a1 1 0 0 1 1-1h3.5a1 1 0 0 1 1 1c0 1.25.2 2.45.57 3.57a1 1 0 0 1-.25 1z"/></svg>
    (555) 410-2750
  </div>
  <a class="abs btn btn-solid header-cta" href="#">Business for sale</a>
</header>

<nav class="abs main-nav">
  <a href="#">Home</a><a href="#">Businesses for Sale</a><a href="#">What we do</a><a href="#">Our people</a><a href="#">Industries</a><a href="#">Blog</a><a href="#">Confidentiality</a><a href="#">Contact</a>
</nav>

<section class="abs hero" role="img" aria-label="Night city skyline with illuminated skyscrapers"></section>
<h1 class="abs hero-title">Venture Transfer<br>Partners</h1>
<p class="abs hero-sub">are a boutique brokerage business, specializing in the sales and marketing of SME businesses throughout Queensland and, the Northern Territory</p>

<form class="abs lead-form">
  <h3>We Will Find You The<br>Perfect Company To Buy</h3>
  <div class="field" style="top:115px">First Name:</div>
  <div class="field" style="top:172px">Last Name:</div>
  <div class="field" style="top:229px">Email:</div>
  <div class="field" style="top:285px">Ph Number:</div>
  <div class="field" style="top:342px;height:136px">Message Here</div>
  <span class="btn btn-solid">Request here</span>
</form>

<div class="abs who-frame"></div>
<div class="abs who-photo" role="img" aria-label="Business team meeting around an office table"></div>
<h2 class="abs section-title who-title">Who We Are</h2>
<div class="abs who-copy">
  <p>Welcome to Venture Transfer Partners. Our specialization is in the marketing and acquisition of closely held businesses throughout Queensland and the Northern Territory. We concentrate in SME businesses in the turnovers of approximately $1,000,000 to $10,000,000 +.</p>
  <p>The combined business experience and industry knowledge of our principal is unparalleled and fully committed to a “customer first always” approach to doing business.Our seller’s benefit from a multi-faceted strategic marketing plan, custom prepared for each seller, no two marketing campaigns are the same. This assures maximum exposure to well-qualified Buyers, while strictly maintaining confidentiality.</p>
  <p>We have the comprehensive knowledge and resources to help our Buyers identify their perfect business acquisition– perhaps even if that business is not currently listed for sale!</p>
  <p>"the whole secret of a successful life is to find out what is one's destiny to do, and then do it." walter pimm</p>
</div>

<div class="abs sold-band"></div>
<div class="abs sold-light"></div>
<h2 class="abs section-title sold-title">Businesses Sold</h2>
<p class="abs sold-sub">Lorem ipsum dolor sit amet, consectetur adipiscing elit, sed do eiusmod tempor incididunt<br>ut labore et dolore magna aliqua. Quis ipsum suspendisse ultrices gravida.</p>

<article class="abs sold-card" style="left:150px">
  <div class="photo" role="img" aria-label="Glass office towers seen from below"></div>
  <h4>Lorem ipsum dolor sit am onsectetur</h4>
  <p>Lorem ipsum dolor sit amet, consectetur adipiscing elied deiusmod tempor incididunt ut labore et dolore ma.</p>
</article>
<article class="abs sold-card" style="left:457px">
  <div class="photo" role="img" aria-label="Blue glass building facade" style="background:linear-gradient(160deg,#7fb3c9,#1f5d78 55%,#0b2f45)"></div>
  <h4>Lorem ipsum dolor sit am onsectetur</h4>
  <p>Lorem ipsum dolor sit amet, consectetur adipiscing elied deiusmod tempor incididunt ut labore et dolore ma.</p>
</article>
<article class="abs sold-card" style="left:765px">
  <div class="photo" role="img" aria-label="Curved glass tower against a sunny sky" style="background:linear-gradient(200deg,#e9f4ff,#5fa4de 50%,#1e5fa3)"></div>
  <h4>Lorem ipsum dolor sit am onsectetur</h4>
  <p>Lorem ipsum dolor sit amet, consectetur adipiscing elied deiusmod tempor incididunt ut labore et dolore ma.</p>
</article>

<h2 class="abs section-title video-title">Our Video</h2>
<p class="abs video-sub">d ut perspiciatis unde omnis iste natus error sit vloolupta tem accusantium doloremque<br>laudantium, totam rem aperiam, eaque ipsa quae ab illo inventore veritatis et qu<br>asi architecto beatae vitae dicta sunt explicaboeim ipsam voluptatem</p>
<div class="abs video" role="img" aria-label="Video still: animated office scene with a businessman seated on a sofa">
  <svg class="abs" style="left:281px;top:105px" width="68" height="68" viewBox="0 0 68 68"><circle cx="34" cy="34" r="33" fill="rgba(60,60,60,.75)"/><circle cx="34" cy="34" r="22" fill="none" stroke="#fff" stroke-width="3"/><path d="M29 24l14 10-14 10z" fill="#fff"/></svg>
  <div class="video-bar">
    <span class="time" style="left:14px">00:00:21</span>
    <span class="time" style="right:14px">00:01:49</span>
    <div class="video-caption">then Venture Transfer Partners represents both sellers<br>and Buyers of Privately held SME Businesses</div>
  </div>
</div>

<section class="abs cta-band"></section>
<h2 class="abs cta-title">Find Deals Before<br>They Come To Market.</h2>
<a class="abs btn btn-outline" href="#">Read more</a>

<h2 class="abs section-title overseas-title">Overseas Buyers</h2>
<p class="abs overseas-copy">Sed ut perspiciatis unde omnis iste natus error sit vloolup ta tem accusantium doloremque laudantium, totam rem aperiam, eaque ipsa quae ab illo inventore veritatis et qu asi architecto beatae vitae dicta sunt explicabo. Nemo en im ipsam voluptatem quia voluptas sit aspernatur aut odit aut fugit, sed quia consequuntur magni dolores eos qlorui ratione voluptatem sequi nesciunt. Neque porro quisqua m est, qui dolorem ipsum quia dolor sit amet, consectetur, adipisci velit, sed quia non numquam eius modi tempora incidunt ut labore et dolore magnam</p>
<a class="abs btn btn-solid overseas-btn" href="#">Read more</a>
<div class="abs overseas-photo" role="img" aria-label="Business people in discussion at a meeting table"></div>

<footer class="abs site-footer"></footer>
<div class="abs brand foot-brand"><span class="dot"></span>Venture Transfer Partners</div>
<p class="abs foot-about">Venture Transfer Partners are a boutique brokerage business, specializing in the sales and marketing of SME businesses throughout Queensland and, the Northern Territory</p>
<p class="abs copyright">Copyright © 2022 All Right Reserved</p>

<div class="abs foot-links">
  <h5 class="foot-h">Links</h5>
  <ul><li>Home</li><li>Businesses for Sale</li><li>What we do</li><li>Our people</li><li>Industries</li><li>Blog</li><li>Confidentiality</li><li>Contact</li></ul>
</div>

<div class="abs foot-contact">
  <h5 class="foot-h">Contact us</h5>
  <div class="contact-row">
    <svg width="14" height="18" viewBox="0 0 14 18"><path fill="#5b4589" d="M7 0a7 7 0 0 0-7 7c0 5 7 11 7 11s7-6 7-11a7 7 0 0 0-7-7zm0 9.5A2.5 2.5 0 1 1 7 4.5a2.5 2.5 0 0 1 0 5z"/></svg>
    <span>Address: 18 Harbour Row<br>Level 4<br>Suite (45)</span>
  </div>
  <div class="contact-row" style="margin-top:20px">
    <svg width="14" height="14" viewBox="0 0 24 24"><path fill="#5b4589" d="M6.6 10.8a15 15 0 0 0 6.6 6.6l2.2-2.2a1 1 0 0 1 1-.25 11.4 11.4 0 0 0 3.6.57 1 1 0 0 1 1 1V20a1 1 0 0 1-1 1A17 17 0 0 1 3 4a1 1 0 0 1 1-1h3.5a1 1 0 0 1 1 1c0 1.25.2 2.45.57 3.57a1 1 0 0 1-.25 1z"/></svg>
    <span>Phone: 555 0142 7788</span>
  </div>
  <div class="contact-row" style="margin-top:20px">
    <svg width="14" height="12" viewBox="0 0 14 12"><rect width="14" height="12" rx="1" fill="#5b4589"/><path d="M1 1.5l6 5 6-5" fill="none" stroke="#fff" stroke-width="1.3"/></svg>
    <span>Email: hello@venturetransfer.example</span>
  </div>
</div>

</body>
</html>
```